IT Network Consultancy - Business Card

kelbrin systems is a IT network consultancy based in London. We're looking for a smart, modern and professional business card design. Our website is here: www.kelbrinsystems.co.uk

Key things that should be included on the card (with examples):

Company Logo
Name
Position / Job Title: Network Consultant
Mobile Phone Number: +44 (0) 7700 900418
Land Line: +44 (0) 1632 960735
Email Address: name@kelbrinsystems.co.uk
Web Site URL: www.kelbrinsystems.co.uk

Target Market(s)

Large enterprise / global companies / corporates

Industry/Entity Type

Business

Requirements
Must have
• Incorporate our logo - which is attached to the project. They are in AI format (can be opened in Inkscape).

The design should be double sided and fit on a UK standard 85mm × 55mm card and be in a format that retains the quality when printed.
Nice to have
• The project does not have to conform to the colour of our website but this should give you inspiration of the style we like.
Should not have
• Bright colours. Pictures are not necessary.

```html
<!DOCTYPE html>
<html lang="en">
<head>
<meta charset="utf-8">
<title>kelbrin systems – Business Card</title>
<link rel="stylesheet" href="https://fonts.googleapis.com/css2?family=Quicksand:wght@500;600&display=swap">
<style>
  :root {
    --page: #ffffff;
    --card: #ffffff;
    --card-edge: #d9dadc;
    --ink: #14191c;
    --accent: #9aa3aa;
    --rule: #a9b0b8;
    --band: #e6e7e9;
  }
  html, body {
    margin: 0;
    padding: 0;
    width: 1200px;
    height: 900px;
    overflow: hidden;
    background: var(--page);
    font-family: "Quicksand", sans-serif;
    color: var(--ink);
  }
  .canvas { position: relative; width: 1200px; height: 900px; }
  .card {
    position: absolute;
    left: 217px; top: 210px;
    width: 725px; height: 469px;
    background: var(--card);
    border: 1px solid var(--card-edge);
    box-shadow: 8px 10px 14px rgba(0,0,0,0.28);
    overflow: hidden;
  }
  .card__band {
    position: absolute;
    left: 22px; top: 173px;
    width: 41px; height: 296px;
    background: var(--band);
  }
  .card__connectors { position: absolute; left: 0; top: 0; }
  .brand {
    position: absolute;
    left: 91px; top: 435px;
    transform-origin: 0 0;
    transform: rotate(-90deg);
    white-space: nowrap;
    font-size: 38px;
    line-height: 46px;
    font-weight: 500;
    letter-spacing: 1px;
    text-transform: uppercase;
    color: var(--ink);
  }
  .identity { position: absolute; left: 353px; top: 112px; }
  .identity__name { margin: 0; font-size: 25px; font-weight: 600; line-height: 32px; }
  .identity__role { margin: 0; font-size: 19px; font-weight: 600; line-height: 26px; }
  .phones { position: absolute; left: 441px; top: 250px; }
  .contact-line {
    margin: 0;
    font-size: 21px;
    font-weight: 600;
    line-height: 29px;
    letter-spacing: 0.6px;
  }
  .web { position: absolute; left: 446px; top: 377px; }
  .web .contact-line { font-size: 20px; letter-spacing: 0.3px; }
</style>
</head>
<body>
<div class="canvas">
  <div class="card">
    <div class="card__band"></div>
    <svg class="card__connectors" width="725" height="469" viewBox="0 0 725 469" aria-hidden="true">
      <line x1="337" y1="0" x2="337" y2="167" stroke="var(--rule)" stroke-width="2"/>
      <circle cx="337" cy="167" r="9" fill="var(--accent)"/>
      <line x1="428" y1="245" x2="725" y2="245" stroke="var(--rule)" stroke-width="2"/>
      <circle cx="428" cy="244" r="10" fill="var(--accent)"/>
      <line x1="428" y1="382" x2="428" y2="469" stroke="var(--rule)" stroke-width="2"/>
      <circle cx="428" cy="382" r="10" fill="var(--accent)"/>
    </svg>
    <div class="brand">Kelbrin Systems</div>
    <div class="identity">
      <p class="identity__name">Your Name</p>
      <p class="identity__role">Network Consultant</p>
    </div>
    <div class="phones">
      <p class="contact-line">+44 (0) 7700 900418</p>
      <p class="contact-line">+44 (0) 1632 960735</p>
    </div>
    <div class="web">
      <p class="contact-line">name@kelbrinsystems.co.uk</p>
      <p class="contact-line">www.kelbrinsystems.co.uk</p>
    </div>
  </div>
</div>
</body>
</html>
```